Hollowmere Capital Stationary Design

We have selected a logo as our winner, we now need a full stationary set to be in the same theme.
Required:
- Letter Head
- Business Card Template
- Custom Envelopes
- A5 Notepad Design (Front cover and content pages. Content pages blank(no lines) but with our branding on them,)
- With Compliments Slip
Updates

Hey All,

We have changed the colour scheme of our logo. Our apologies if anyone has begun designing based off the old scheme. Please see the updated scheme in the brief,

Oliver

Target Market(s)

Target market is experienced property developers and financial institutions.

Industry/Entity Type

Commercial Finance

Font styles to use
Serif

Colors
0054AA
0677BA
7BADD7
CADEEF
E8F1F8
0094D4
00A9DD
6FCCEA
C7EBF8
E9F6FB
00AB8E
00BBA5
67D7C9
C6EFE9
E9F9F6
59FF00
82FF00
B8FF75
E3FFCB
F4FFEA

```html
<!DOCTYPE html>
<html lang="en">
<head>
<meta charset="utf-8">
<title>Hollowmere Capital Letterhead</title>
<link href="https://fonts.googleapis.com/css2?family=Open+Sans:wght@400;600;700&family=Roboto:wght@400&display=swap" rel="stylesheet">
<style>
  :root {
    --backdrop: #e6e6e6;
    --paper: #f8f8f8;
    --brand-blue: #1f3d94;
    --brand-green: #22803e;
    --body-text: #5c5c5c;
    --contact-text: #333333;
    --signature-tone: #e4e7ee;
  }
  * { margin: 0; padding: 0; box-sizing: border-box; }
  html, body {
    width: 1153px;
    height: 1200px;
    overflow: hidden;
    background: var(--backdrop);
  }
  .letterhead {
    position: absolute;
    left: 151px;
    top: 8px;
    width: 850px;
    height: 1184px;
    background: var(--paper);
    font-family: "Open Sans", Arial, sans-serif;
    overflow: hidden;
  }
  .brand {
    position: absolute;
    left: 84px;
    top: 86px;
    display: flex;
    align-items: center;
    gap: 10px;
  }
  .brand-square {
    width: 18px;
    height: 18px;
    background: var(--brand-blue);
  }
  .brand-name {
    font-family: "Open Sans", Arial, sans-serif;
    font-weight: 700;
    font-size: 25px;
    color: var(--brand-blue);
    letter-spacing: 0.2px;
  }
  .contact {
    position: absolute;
    left: 562px;
    top: 56px;
    font-family: "Roboto", Arial, sans-serif;
    font-size: 14px;
    line-height: 18.5px;
    color: var(--contact-text);
  }
  .contact-address { margin-bottom: 7px; }
  .contact-line {
    display: flex;
    align-items: center;
    gap: 7px;
  }
  .contact-line svg { width: 14px; height: 14px; fill: var(--brand-green); flex: none; }
  .letter-body {
    position: absolute;
    left: 84px;
    top: 296px;
    width: 682px;
    font-size: 15.4px;
    line-height: 22.4px;
    color: var(--body-text);
  }
  .letter-body p {
    text-align: justify;
    margin-bottom: 22px;
  }
  .letter-body .salutation,
  .letter-body .closing { text-align: left; }
  .signature {
    position: absolute;
    left: 84px;
    top: 880px;
    width: 100px;
    height: 92px;
    background: var(--signature-tone);
  }
  .footer-band {
    position: absolute;
    left: 0;
    bottom: 0;
    width: 850px;
    height: 15px;
  }
</style>
</head>
<body>
  <main class="letterhead">
    <div class="brand">
      <span class="brand-square"></span>
      <span class="brand-name">Hollowmere Capital</span>
    </div>

    <address class="contact" style="font-style: normal;">
      <div class="contact-address">Marlow Lane 42<br>City Fenwick Bay USA</div>
      <div class="contact-line">
        <svg viewBox="0 0 16 16" aria-hidden="true"><path d="M2 6c0-2 3-3 6-3s6 1 6 3v1h-3V5.5H5V7H2zM4 8h8l2 5H2zm4 1.5a1.5 1.5 0 1 0 0 3 1.5 1.5 0 0 0 0-3z"/></svg>
        <span>555.204.7316</span>
      </div>
      <div class="contact-line">
        <svg viewBox="0 0 16 16" aria-hidden="true"><path d="M1 4h14v1L8 9 1 5zm0 2.5 7 4 7-4V12H1z"/></svg>
        <span>info@hollowmerecapital.com</span>
      </div>
      <div class="contact-line">
        <svg viewBox="0 0 16 16" aria-hidden="true"><circle cx="8" cy="8" r="6.5"/><path d="M5 4c1 1 2 1 2 3s-2 1-2 3M10 3.5c-1 2 1 3 2 3M9 13c0-2 2-2 3-3" stroke="#f8f8f8" stroke-width="1.3" fill="none"/></svg>
        <span>www.hollowmerecapital.com</span>
      </div>
    </address>

    <section class="letter-body">
      <p class="salutation">Dear customer,</p>
      <p>Lorem ipsum dolor sit amet, consectetur adipisicing elit, sed do eiusmod tempor incididunt ut labore et dolore magna aliqua. Ut enim ad minim veniam, quis nostrud exercitation ullamco laboris nisi ut aliquip ex ea commodo consequat. Duis aute irure dolor in reprehenderit in voluptate velit esse cillum dolore eu fugiat nulla pariatur. Excepteur sint occaecat cupidatat non proident, sunt in culpa qui officia deserunt mollit anim id est laborum.</p>
      <p>Lorem ipsum dolor sit amet, consectetur adipisicing elit, sed do eiusmod tempor incididunt ut labore et dolore magna aliqua. Ut enim ad minim veniam, quis nostrud exercitation ullamco laboris nisi ut aliquip ex ea commodo consequat. Duis aute irure dolor in reprehenderit in voluptate velit esse cillum dolore eu fugiat nulla pariatur. Excepteur sint occaecat cupidatat non proident, sunt in culpa qui officia deserunt mollit anim id est laborum.</p>
      <p>Lorem ipsum dolor sit amet, consectetur adipisicing elit, sed do eiusmod tempor incididunt ut labore et dolore magna aliqua. Ut enim ad minim veniam, quis nostrud exercitation ullamco laboris nisi ut aliquip ex ea commodo consequat. Duis aute irure dolor in reprehenderit in voluptate velit esse cillum dolore eu fugiat nulla pariatur. Excepteur sint occaecat cupidatat non proident, sunt in culpa qui officia deserunt mollit anim id est laborum.</p>
      <p>Lorem ipsum dolor sit amet, consectetur adipisicing elit, sed do eiusmod tempor incididunt ut labore et dolore magna aliqua. Ut enim ad minim veniam, quis nostrud exercitation ullamco laboris nisi ut aliquip ex ea commodo consequat. Duis aute irure dolor in reprehenderit.</p>
      <p class="closing">Yours Sincerely,</p>
    </section>

    <div class="signature" role="img" aria-label="Handwritten signature of the sender"></div>

    <svg class="footer-band" viewBox="0 0 850 15" preserveAspectRatio="none" aria-hidden="true">
      <polygon points="0,0 662,0 643,15 0,15" fill="var(--brand-blue)"/>
      <polygon points="667,0 850,0 850,15 648,15" fill="var(--brand-green)"/>
    </svg>
  </main>
</body>
</html>
```